PRESENTATION FOLDER DESIGN

I would like to design a presentation folder that is 6 x 9 with 2 x 4 inch pockets.
I have attached the logo to use as well as the template for the presentation folder.

I also included the front and back of the business cards so that you can see the overall look I am trying to go for as well as the information to have on there.

The presentation folder will be used to send out an invitation to a conference for dentists.

Target Market(s)

dentists

Font styles to use
Sans Serif

Requirements
Must have
• The clours must be the same as on the logo.
• On the cover, I would like a title in bold large letters that says:
• PLEASE JOIN US FOR OUR EXCLUSIVE EVENTS
• FOR DENTAL PROFESSIONALS
• *eligible for CE credits
• I would like to have this picture on the cover as well.
• ON THE BACK, i WOULD THE COLOURS TO BE THE BLUE FROM THE LOGO AND THE WRITING IN WHITE.
• THE INSIDE FLAPS MUST BE IN THE BLUE BUT THE INSIDE OF THE FOLDER SHOULD BE IN ORANGE.
• ON THE INSIDE FLAPS WE SHOULD WRITE:
• ON THE LEFT FLAP: I WANT TO PURCHASE A CLINIC
• ON THE RIGHT FLAP: I WANT TO SELL MY CLINIC

```html
<!DOCTYPE html>
<html lang="en">
<head>
<meta charset="utf-8">
<title>Denquaro Presentation Folder</title>
<link rel="stylesheet" href="https://fonts.googleapis.com/css2?family=Montserrat:wght@400;500;600;700;800&family=Raleway:wght@400;500&display=swap">
<style>
  :root{
    --blue:#2cbfd6;
    --blue-soft:#7fd3e0;
    --orange:#f06423;
    --orange-deep:#e0561c;
    --white:#ffffff;
    --ink:#4a4a4a;
    --page:#ffffff;
  }
  *{box-sizing:border-box;margin:0;padding:0}
  html,body{width:966px;height:1200px;overflow:hidden;background:var(--page)}
  body{position:relative;font-family:"Montserrat",sans-serif}

  .panel{position:absolute}

  /* back cover */
  .back-cover{left:144px;top:80px;width:326px;height:489px;background:var(--blue);overflow:hidden}
  .back-cover .site-rule{position:absolute;top:30px;left:0;right:0;display:flex;align-items:center;gap:6px;color:var(--white);font-weight:700;font-size:12px;white-space:nowrap}
  .back-cover .site-rule::before,.back-cover .site-rule::after{content:"";flex:1;height:1px;background:var(--white)}
  .back-cover .brand{position:absolute;top:176px;left:0;right:0;text-align:center;color:var(--white);font-weight:400;font-size:26px;letter-spacing:.5px}

  /* front cover */
  .front-cover{left:483px;top:80px;width:326px;height:489px;background:var(--white);overflow:hidden}
  .front-cover .top-band{position:absolute;left:0;top:0;width:100%;height:25px;background:var(--blue)}
  .front-cover .photo{position:absolute;left:0;top:25px;width:100%;height:236px;background:linear-gradient(135deg,#f4f8fa 0%,#dfeef2 45%,#9fdbe6 70%,#e8eef0 100%)}
  .front-cover .wedges{position:absolute;left:0;top:215px;width:326px;height:80px}
  .front-cover .brand{position:absolute;top:336px;left:0;right:0;text-align:center;color:var(--blue);font-weight:400;font-size:20px;letter-spacing:.3px}
  .front-cover .headline{position:absolute;left:32px;right:32px;top:391px;border-top:1px solid var(--blue);padding-top:7px;text-align:center}
  .front-cover h1{color:var(--blue);font-weight:800;font-size:20.5px;line-height:26px;letter-spacing:.2px;white-space:nowrap}
  .front-cover .credits{margin-top:3px;color:var(--orange);font-weight:500;font-size:7.8px;letter-spacing:.1px;white-space:nowrap}

  /* inside spread */
  .inside{left:138px;top:590px;width:667px;height:518px;background:var(--orange)}
  .inside .spine{position:absolute;left:333px;top:0;width:8px;height:100%;background:linear-gradient(90deg,var(--orange),var(--orange-deep),var(--orange))}

  .sheet{position:absolute;background:var(--white);padding:18px 17px 0 17px;overflow:hidden}
  .sheet-left{left:14px;top:65px;width:297px;height:290px}
  .sheet-right{left:370px;top:105px;width:283px;height:250px;padding:18px 15px 0 17px}
  .sheet-head{display:flex;justify-content:space-between;align-items:flex-end;border-bottom:2px solid var(--blue);padding-bottom:3px;margin-bottom:10px}
  .sheet-head .brand{color:var(--blue);font-weight:400;font-size:14px}
  .sheet-head .site{color:var(--blue);font-weight:700;font-size:8.5px;margin-bottom:4px}
  .sheet p{font-family:"Raleway",sans-serif;color:var(--ink);font-size:8.3px;line-height:12.6px;margin-bottom:12px}
  .sheet p.lead{font-family:"Montserrat",sans-serif;color:var(--orange);font-weight:600;font-size:7.9px;text-transform:uppercase}
  .sheet-right p{font-size:7.6px;line-height:11px;margin-bottom:10px}
  .sheet-right p.lead{font-size:7.3px}

  .pocket{position:absolute;top:337px;height:181px;background:var(--blue);overflow:hidden}
  .pocket-left{left:0;width:333px;border-top-right-radius:70px 110px}
  .pocket-right{left:341px;width:326px;border-top-left-radius:70px 110px}
  .pocket .intro{position:absolute;top:17px;width:200px;text-align:center;color:var(--white)}
  .pocket-left .intro{left:46px}
  .pocket-right .intro{left:87px}
  .pocket .kicker{display:flex;align-items:center;gap:3px;font-weight:400;font-size:11.5px}
  .pocket .kicker::before,.pocket .kicker::after{content:"";flex:1;height:1px;background:var(--white);max-width:42px;margin:0 auto}
  .pocket .action{font-weight:700;font-size:14.5px;margin-top:2px;white-space:nowrap}

  .card{position:absolute;top:66px;width:150px;height:80px;background:var(--white);border-radius:4px;text-align:center}
  .pocket-left .card{left:126px}
  .pocket-right .card{left:69px}
  .card .brand{margin-top:22px;color:var(--blue);font-weight:400;font-size:14px}
  .card .services{margin-top:12px;color:var(--orange);font-weight:400;font-size:3.4px;line-height:5px;letter-spacing:.1px}
  .slit{position:absolute;height:1px;width:30px;background:#1f7e8e;transform:rotate(-45deg)}
</style>
</head>
<body>

  <section class="panel back-cover" aria-label="Back cover">
    <div class="site-rule">www.denquaro.ca</div>
    <div class="brand">DENQUARO</div>
  </section>

  <section class="panel front-cover" aria-label="Front cover">
    <div class="top-band"></div>
    <div class="photo" role="img" aria-label="Photograph of a light blue dental chair and instruments in a bright clinic"></div>
    <svg class="wedges" viewBox="0 0 326 80" aria-hidden="true">
      <polygon points="0,50 0,80 326,30 326,14" fill="var(--blue)"/>
      <polygon points="60,20 326,46 326,62" fill="var(--orange)"/>
      <polygon points="0,28 0,50 150,27" fill="var(--blue)"/>
      <polygon points="220,14 326,0 326,30" fill="var(--blue)"/>
    </svg>
    <div class="brand">DENQUARO</div>
    <div class="headline">
      <h1>PLEASE JOIN US FOR<br>OUR EXCLUSIVE EVENTS</h1>
      <div class="credits">FOR DENTAL PROFESSIONALS ELIGIBLE FOR CE CREDITS</div>
    </div>
  </section>

  <section class="panel inside" aria-label="Inside of folder">
    <div class="spine"></div>

    <article class="sheet sheet-left">
      <header class="sheet-head"><span class="brand">DENQUARO</span><span class="site">www.denquaro.ca</span></header>
      <p>Lorem ipsum dolor sit amet, consectetuer adipiscing elit, sed diam nonummy nibh euismod tincidunt ut laoreet dolore magna aliquam erat volutpat.</p>
      <p class="lead">Ut wisi enim ad minim veniam, quis nostrud exerci tation ullamcorper suscipit lobortis nisl ut aliquip ex ea commodo consequat.</p>
      <p>Duis autem vel eum iriure dolor in hendrerit in vulputate velit esse molestie consequat, vel illum dolore eu feugiat nulla facilisis at vero eros et accumsan et iusto odio dignissim qui blandit praesent luptatum zzril delenit augue duis dolore te feugait nulla facilisi.</p>
      <p>Lorem ipsum dolor sit amet, cons ectetuer adipiscing elit, sed diam nonummy nibh euismod tincidunt ut laoreet dolore</p>
    </article>

    <article class="sheet sheet-right">
      <header class="sheet-head"><span class="brand">DENQUARO</span><span class="site">www.denquaro.ca</span></header>
      <p>Lorem ipsum dolor sit amet, consectetuer adipiscing elit, sed diam nonummy nibh euismod tincidunt ut laoreet dolore magna aliquam erat volutpat.</p>
      <p class="lead">Ut wisi enim ad minim veniam, quis nostrud exerci tation ullamcorper suscipit lobortis nisl ut aliquip ex ea commodo consequat.</p>
      <p>Duis autem vel eum iriure dolor in hendrerit in vulputate velit esse molestie consequat, vel illum dolore eu feugiat nulla facilisis at vero eros et accumsan et iusto odio dignissim qui blandit praesent luptatum zzril delenit augue duis dolore te feugait nulla facilisi.</p>
      <p>Lorem ipsum dolor sit amet, cons ectetuer adipiscing elit, sed diam nonummy nibh euismod tincidunt ut laoreet dolore</p>
    </article>

    <div class="pocket pocket-left">
      <div class="intro">
        <div class="kicker">I WANT TO</div>
        <div class="action">PURCHASE A CLINIC</div>
      </div>
      <div class="slit" style="left:118px;top:74px"></div>
      <div class="card">
        <div class="brand">DENQUARO</div>
        <div class="services">CONSEIL | FISCALITÉ | TRANSITIONS DE CLINIQUE<br>BUSINESS ADVICE | TAXATION | CLINIC TRANSITIONS</div>
      </div>
      <div class="slit" style="left:262px;top:138px"></div>
    </div>

    <div class="pocket pocket-right">
      <div class="intro">
        <div class="kicker">I WANT TO</div>
        <div class="action">SELL MY CLINIC</div>
      </div>
      <div class="slit" style="left:61px;top:74px"></div>
      <div class="card">
        <div class="brand">DENQUARO</div>
        <div class="services">CONSEIL | FISCALITÉ | TRANSITIONS DE CLINIQUE<br>BUSINESS ADVICE | TAXATION | CLINIC TRANSITIONS</div>
      </div>
      <div class="slit" style="left:205px;top:138px"></div>
    </div>
  </section>

</body>
</html>
```